We need a business card design for a new soccer program based in Melbourne, Victoria, Australia.
Coaching kids from 2 through to 14 develop social, motor and soccer skills, in a fun and friendly non-competitive environment.
Our company colours are blue and orange as seen in the logo attached below. However, we are happy for the font to be any modern colour that looks professional.
Target Market(s)
Mums and dads
Industry/Entity Type
Business
Contact Information for Business Card
business name: Bright Kick Soccer
Marko Delvino Director- 0451 738 015
Luke Ferrano Director- 0419 856 371
Tomas Kovalenko Head Coach
email: marko@brightkicksoccer.com.au
website: www.brightkicksoccer.com.au
Coaching kids from 2-14
https://www.kidsclubhub.net/brightkicksoccer (facebook page not required unless it looks good without being clustered)
Look and feel

```html
<!DOCTYPE html>
<html lang="en">
<head>
<meta charset="utf-8">
<title>Bright Kick Soccer – Business Card</title>
<link rel="stylesheet" href="https://fonts.googleapis.com/css2?family=Open+Sans:wght@400;600;700;800&display=swap">
<style>
  :root {
    --orange: #f0961f;
    --blue: #1c3a8f;
    --paper: #f4f3f0;
    --ink: #1f1f1f;
    --backdrop: #d6d6d4;
    --white: #ffffff;
  }
  * { box-sizing: border-box; margin: 0; padding: 0; }
  html, body {
    width: 1200px; height: 1200px; overflow: hidden;
    background: var(--backdrop);
    font-family: "Open Sans", Arial, sans-serif;
  }
  .canvas { position: relative; width: 1200px; height: 1200px; }
  .card {
    position: absolute; left: 150px; width: 900px; height: 514px;
    background: var(--paper); overflow: hidden;
    box-shadow: 0 8px 24px rgba(0,0,0,0.18);
  }
  .card--front { top: 60px; }
  .card--back { top: 626px; }

  /* Front */
  .front__band-left {
    position: absolute; left: 0; top: 0; width: 150px; height: 100%;
    background: var(--orange);
  }
  .front__band-right {
    position: absolute; right: 0; top: 0; width: 90px; height: 100%;
    background: var(--blue);
  }
  .brand {
    position: absolute; left: 150px; right: 90px; top: 0; bottom: 0;
    display: flex; align-items: center; justify-content: center; gap: 22px;
  }
  .brand__mark {
    width: 70px; height: 70px; border-radius: 50%;
    background: var(--orange); flex: none;
  }
  .brand__name {
    font-weight: 800; font-size: 64px; line-height: 1.02;
    color: var(--blue); text-transform: uppercase; letter-spacing: -1px;
  }

  /* Back */
  .back__orange {
    position: absolute; inset: 0;
    background: var(--orange);
    clip-path: polygon(125px 0, 900px 0, 900px 514px, 255px 514px);
  }
  .back__blue {
    position: absolute; left: 250px; top: 196px; right: 0; bottom: 0;
    background: var(--blue);
  }
  .person {
    position: absolute; left: 300px; top: 20px; color: var(--white);
  }
  .person__name { font-size: 58px; font-weight: 400; line-height: 1.05; letter-spacing: 0.5px; }
  .person__role { font-size: 26px; font-weight: 400; margin-left: 30px; line-height: 1.2; }
  .person__email {
    position: absolute; right: 150px; top: 146px;
    font-size: 16px; color: var(--white);
  }
  .contact {
    position: absolute; left: 290px; top: 222px; color: var(--white);
  }
  .contact__web { font-size: 30px; font-weight: 600; margin-left: 80px; line-height: 1.3; }
  .contact__social { font-size: 18px; font-weight: 600; margin-left: 50px; margin-top: 8px; }
  .contact__directors { margin-top: 36px; font-size: 24px; font-weight: 400; line-height: 1.5; }
  .tagline {
    position: absolute; left: 44px; top: 400px;
    font-size: 22px; font-weight: 700; line-height: 1.15; color: var(--ink);
  }
</style>
</head>
<body>
<main class="canvas">
  <section class="card card--front" aria-label="Business card front">
    <div class="front__band-left"></div>
    <div class="front__band-right"></div>
    <div class="brand">
      <span class="brand__mark"></span>
      <span class="brand__name">Bright<br>Kick<br>Soccer</span>
    </div>
  </section>

  <section class="card card--back" aria-label="Business card back">
    <div class="back__orange"></div>
    <div class="back__blue"></div>
    <div class="person">
      <p class="person__name">Tomas Kovalenko</p>
      <p class="person__role">Head Coach</p>
    </div>
    <p class="person__email">email: marko@brightkicksoccer.com.au</p>
    <div class="contact">
      <p class="contact__web">www.brightkicksoccer.com.au</p>
      <p class="contact__social">https://www.kidsclubhub.net/brightkicksoccer</p>
      <p class="contact__directors">Luke Ferrano Director- 0419 856 371<br>Marko Delvino Director- 0451 738 015</p>
    </div>
    <p class="tagline">Coaching kids<br>from 2-14</p>
  </section>
</main>
</body>
</html>
```